" SOMOS UM ESCRITORIO DE ADVOCACIA QUE TRABALHA NA AREA DO DIREITO TRIBUTARIO, OU SEJA, PROCURANDO MAXIMIZAR OS GANHOS DOS CLIENTES COM REDUÇÃO DE IMPOSTOS, BEM COMO COM REORGANIZAÇÃO SOCIETARIA PARA PROTEGER O PATRIMONIO DOS SOCIOS. "

```html
<!DOCTYPE html>
<html lang="pt-BR">
<head>
<meta charset="utf-8">
<title>Vasco Teixeira — Papel Timbrado</title>
<link href="https://fonts.googleapis.com/css2?family=Cormorant+Garamond:wght@400;500&family=Montserrat:wght@400&display=swap" rel="stylesheet">
<style>
  :root {
    --backdrop: #1f2527;
    --paper: #ffffff;
    --gold: #b8913a;
    --gold-light: #e2c77c;
    --ink: #4a4a4a;
    --watermark: #f1f1f1;
  }
  * { margin: 0; padding: 0; box-sizing: border-box; }
  html, body {
    width: 1200px;
    height: 1200px;
    overflow: hidden;
    background: var(--backdrop);
  }
  .letterhead {
    position: absolute;
    left: 232px;
    top: 80px;
    width: 736px;
    height: 1040px;
    background: var(--paper);
    box-shadow: 0 12px 40px rgba(0,0,0,0.35);
  }
  .brand {
    position: absolute;
    top: 56px;
    right: 70px;
    display: flex;
    flex-direction: column;
    align-items: center;
    gap: 8px;
  }
  .brand-dot {
    width: 26px;
    height: 26px;
    border-radius: 50%;
    background: var(--gold);
  }
  .brand-name {
    font-family: "Cormorant Garamond", serif;
    font-weight: 500;
    font-size: 24px;
    letter-spacing: 3px;
    text-transform: uppercase;
    color: var(--gold);
  }
  .brand-tagline {
    font-family: "Cormorant Garamond", serif;
    font-weight: 500;
    font-size: 10px;
    letter-spacing: 3px;
    text-transform: uppercase;
    color: var(--gold);
  }
  .watermark {
    position: absolute;
    left: 218px;
    top: 330px;
    width: 300px;
    height: 360px;
    border-radius: 46% 46% 50% 50%;
    background: radial-gradient(circle at 50% 45%, var(--watermark), #f7f7f7 70%, var(--paper));
  }
  .contact {
    position: absolute;
    right: 70px;
    bottom: 60px;
    font-family: "Montserrat", sans-serif;
    font-size: 11px;
    line-height: 1.6;
    color: var(--ink);
    text-align: left;
  }
  .edge-tab {
    position: absolute;
    right: 0;
    bottom: 110px;
    width: 12px;
    height: 64px;
    background: linear-gradient(180deg, var(--gold-light), var(--gold));
  }
</style>
</head>
<body>
  <main class="letterhead">
    <header class="brand">
      <span class="brand-dot"></span>
      <span class="brand-name">Vasco Teixeira</span>
      <span class="brand-tagline">Advocacia Tributária</span>
    </header>

    <div class="watermark" role="img" aria-label="Marca d'água clara e grande do símbolo do escritório ao centro da folha"></div>

    <address class="contact">
      Rua das Acácias, 120, Centro<br>
      (11) 3200-4500<br>
      contato@teixeiraadv.com.br<br>
      www.teixeiraadv.com.br
    </address>

    <span class="edge-tab"></span>
  </main>
</body>
</html>
```